DESIGN OF STATIONERY - TALVORA MED

WE WORK IN THE FIELD OF HEALTH (IMAGING: MRI - CT ETC.).
WE WOULD LIKE TO CREATE THE ENTIRE STATIONERY DESIGN : LETTERHEAD, BUSINESS CARD, CALENDAR, INVOICES, CD HOLDER, ETC.

Target Market(s)

PERSONS UNDERTAKING HEALTH EXAMINATIONS

```html
<!DOCTYPE html>
<html lang="en">
<head>
<meta charset="utf-8">
<title>Talvora Med – Business Card</title>
<link rel="stylesheet" href="https://fonts.googleapis.com/css2?family=Raleway:wght@700&family=Roboto:wght@400&display=swap">
<style>
  :root {
    --page-bg: #e6e3df;
    --card-bg: #f4f5f6;
    --card-edge: #b9bcbf;
    --brand-blue: #1f4f8f;
    --brand-green: #1f8a64;
    --text-grey: #4a4d52;
    --icon-blue: #1f4f8f;
    --divider: #4a4d52;
  }
  * { margin: 0; padding: 0; box-sizing: border-box; }
  html, body {
    width: 1200px;
    height: 1090px;
    overflow: hidden;
    background: var(--page-bg);
  }
  .canvas {
    position: relative;
    width: 1200px;
    height: 1090px;
  }
  .business-card {
    position: absolute;
    left: 100px;
    top: 267px;
    width: 1000px;
    height: 556px;
    background: var(--card-bg);
    border: 1px solid var(--card-edge);
    box-shadow: 0 10px 30px rgba(0,0,0,0.12);
  }
  .brand {
    position: absolute;
    left: 505px;
    top: 78px;
    display: flex;
    align-items: center;
    gap: 14px;
  }
  .brand-dot {
    width: 22px;
    height: 22px;
    border-radius: 50%;
    background: var(--brand-green);
  }
  .brand-name {
    font-family: "Raleway", sans-serif;
    font-weight: 700;
    font-size: 50px;
    letter-spacing: 0.5px;
    color: var(--brand-blue);
  }
  .holder {
    position: absolute;
    left: 77px;
    top: 218px;
  }
  .holder-name {
    font-family: "Raleway", sans-serif;
    font-weight: 700;
    font-size: 32px;
    color: var(--brand-blue);
    line-height: 1.1;
  }
  .holder-title {
    font-family: "Raleway", sans-serif;
    font-weight: 700;
    font-size: 20px;
    color: var(--brand-green);
    margin-top: 4px;
  }
  .address {
    position: absolute;
    left: 77px;
    top: 320px;
    font-family: "Roboto", sans-serif;
    font-size: 22px;
    line-height: 31px;
    color: var(--text-grey);
  }
  .contacts {
    position: absolute;
    left: 77px;
    top: 417px;
    display: flex;
    align-items: center;
    font-family: "Roboto", sans-serif;
    font-size: 22px;
    color: var(--text-grey);
  }
  .contact-list { list-style: none; }
  .contact-list li {
    display: flex;
    align-items: center;
    gap: 8px;
    height: 31px;
  }
  .contact-list svg { width: 22px; height: 22px; fill: var(--icon-blue); flex: none; }
  .contact-divider {
    width: 2px;
    height: 56px;
    background: var(--divider);
    margin: 0 16px 0 18px;
  }
</style>
</head>
<body>
<div class="canvas">
  <section class="business-card">
    <div class="brand">
      <span class="brand-dot"></span>
      <span class="brand-name">Talvora Med</span>
    </div>

    <div class="holder">
      <div class="holder-name">Daniel Harrow</div>
      <div class="holder-title">President</div>
    </div>

    <address class="address" style="font-style:normal">
      Carlton House, 42 Redmond<br>Ave, London SW4 7QT
    </address>

    <div class="contacts">
      <ul class="contact-list">
        <li>
          <svg viewBox="0 0 24 24" aria-hidden="true"><path d="M6.6 10.8a15.1 15.1 0 0 0 6.6 6.6l2.2-2.2c.3-.3.7-.4 1-.2 1.1.4 2.3.6 3.6.6.6 0 1 .4 1 1V20c0 .6-.4 1-1 1A17 17 0 0 1 3 4c0-.6.4-1 1-1h3.5c.6 0 1 .4 1 1 0 1.3.2 2.5.6 3.6.1.3 0 .7-.2 1z"/></svg>
          (555) 318-4200
        </li>
        <li>
          <svg viewBox="0 0 24 24" aria-hidden="true"><path d="M7 3h10v5H7zM4 9h16a2 2 0 0 1 2 2v6h-4v4H6v-4H2v-6a2 2 0 0 1 2-2zm4 7v3h8v-3zm10-4.5a1 1 0 1 0 0 2 1 1 0 0 0 0-2z"/></svg>
          (555) 318-4637
        </li>
      </ul>
      <span class="contact-divider"></span>
      <ul class="contact-list">
        <li>
          <svg viewBox="0 0 24 24" aria-hidden="true"><path d="M2 5h20v14H2zm2 2v.5l8 5.5 8-5.5V7zm0 2.9V17h16V9.9l-8 5.5z"/></svg>
          info@talvoramed.com
        </li>
        <li>
          <svg viewBox="0 0 24 24" aria-hidden="true"><path d="M12 2a10 10 0 1 0 0 20 10 10 0 0 0 0-20zm6.9 9h-3a15 15 0 0 0-1.2-5.6A8 8 0 0 1 18.9 11zM12 4.1c.9 1.2 1.8 3.5 1.9 6.9h-3.8c.1-3.4 1-5.7 1.9-6.9zM9.3 5.4A15 15 0 0 0 8.1 11h-3a8 8 0 0 1 4.2-5.6zM5.1 13h3a15 15 0 0 0 1.2 5.6A8 8 0 0 1 5.1 13zm6.9 6.9c-.9-1.2-1.8-3.5-1.9-6.9h3.8c-.1 3.4-1 5.7-1.9 6.9zm2.7-1.3a15 15 0 0 0 1.2-5.6h3a8 8 0 0 1-4.2 5.6z"/></svg>
          www.talvoramed.com
        </li>
      </ul>
    </div>
  </section>
</div>
</body>
</html>
```